New product NuraLeaf Box Packaging Design

We are looking for a product packaging design concept.

The product name is NuraLeaf, Logo is attached in this post.
NuraLeaf is an infant drop, with probiotic infused with Vitamin D in one. This probiotic + Vitamin D drop is for baby, and it is great for baby's digestive system, and improve immune system.
It is meant for drop per daily use.
It will be in a box, so we are looking for the box design concept.

Although it sounds like a pharmaceutical product, we want the packaging design to look more consumer-friendly, and baby-like.
North American style, modern, and baby product looking, is what we are expecting for this project. Product package needs to visually convey that it is for digestive system & it is for baby.

Some of the brands that has similar concept and products are: Velmora, K Pearls, Hartwell Probiotic Baby, and Quenby's Naturals. Images of the products from these brands are attached for your reference.

We are ONLY looking for the box design for now.
Feel free to contact me for any questions.

Reason: Holiday Season. Office closed. We will be ready to choose the designer in a few days. Thank you!

Baby

Baby

• Our Logo, and baby like design, and visuals that indicate it is great for Baby's digestive system and immune system.

```html
<!DOCTYPE html>
<html lang="en">
<head>
<meta charset="utf-8">
<title>NuraLeaf Baby Probiotic + Vitamin D Drops – Box Panels</title>
<link href="https://fonts.googleapis.com/css2?family=Comfortaa:wght@400;700&family=Oswald:wght@600&family=Permanent+Marker&family=Yanone+Kaffeesatz:wght@300;400&display=swap" rel="stylesheet">
<style>
  :root {
    --lime: #b5d334;
    --teal: #2bab74;
    --leaf: #2bb673;
    --leaf-dark: #1f9a5e;
    --orange: #f7ae4f;
    --orange-text: #f4a83c;
    --ink: #111111;
    --white: #ffffff;
    --paper: #f7f7f5;
    --fold: #e3e3e0;
    --skin: #f3c29a;
    --hair: #e2a23a;
    --shirt: #8fbf3a;
  }
  html, body {
    margin: 0;
    padding: 0;
    width: 1200px;
    height: 1200px;
    overflow: hidden;
    background: var(--paper);
  }
  .canvas {
    position: relative;
    width: 1200px;
    height: 1200px;
  }
  .box-panels {
    position: absolute;
    left: 180px;
    top: 100px;
    width: 840px;
    height: 1000px;
    display: flex;
    box-shadow: 0 12px 40px rgba(0,0,0,0.12);
  }
  .panel {
    position: relative;
    height: 1000px;
    overflow: hidden;
    background: var(--white);
  }
  .panel + .panel { border-left: 1px solid var(--fold); }
  .panel-side { width: 120px; }
  .panel-front { width: 600px; }
  .panel-art {
    position: absolute;
    inset: 0;
  }

  /* front panel */
  .brand-name {
    position: absolute;
    left: 80px;
    top: 100px;
    margin: 0;
    font-family: "Comfortaa", sans-serif;
    font-weight: 700;
    font-size: 58px;
    line-height: 1;
    color: var(--teal);
    display: flex;
    align-items: center;
    gap: 14px;
  }
  .brand-dot {
    width: 24px;
    height: 24px;
    border-radius: 50%;
    background: var(--teal);
  }
  .range-name {
    position: absolute;
    left: 150px;
    top: 170px;
    margin: 0;
    font-family: "Comfortaa", sans-serif;
    font-weight: 400;
    font-size: 100px;
    line-height: 1;
    color: var(--orange-text);
  }
  .product-name {
    position: absolute;
    left: 20px;
    width: 560px;
    top: 295px;
    margin: 0;
    font-family: "Oswald", sans-serif;
    font-weight: 600;
    font-size: 60px;
    line-height: 1;
    color: var(--ink);
    text-align: center;
  }
  .format-label {
    position: absolute;
    left: 345px;
    top: 478px;
    width: 170px;
    margin: 0;
    text-align: center;
    font-family: "Permanent Marker", "Comic Sans MS", cursive;
    font-size: 40px;
    line-height: 1;
    color: var(--ink);
  }
  .benefit {
    position: absolute;
    left: 300px;
    top: 615px;
    width: 290px;
    margin: 0;
    font-family: "Yanone Kaffeesatz", sans-serif;
    font-weight: 400;
    font-size: 38px;
    line-height: 1.05;
    color: var(--white);
    text-align: center;
  }
  .details {
    position: absolute;
    left: 18px;
    top: 822px;
    margin: 0;
    padding: 0;
    list-style: none;
    font-family: "Yanone Kaffeesatz", sans-serif;
    font-size: 32px;
    color: var(--ink);
  }
  .details li {
    width: 230px;
    border-bottom: 2px solid var(--ink);
    line-height: 34px;
    margin-bottom: 2px;
  }
  .dose {
    position: absolute;
    left: 435px;
    top: 860px;
    width: 150px;
    margin: 0;
    text-align: center;
    color: var(--ink);
  }
  .dose-amount {
    display: block;
    font-family: "Yanone Kaffeesatz", sans-serif;
    font-weight: 300;
    font-size: 64px;
    line-height: 1;
  }
  .dose-unit {
    display: block;
    font-family: "Comfortaa", sans-serif;
    font-size: 22px;
    margin-top: 4px;
  }

  /* right side panel */
  .side-label {
    position: absolute;
    left: 16px;
    top: 70px;
    width: 88px;
    height: 70px;
    margin: 0;
    background: var(--teal);
    color: var(--white);
    font-family: "Yanone Kaffeesatz", sans-serif;
    font-size: 16px;
    display: flex;
    align-items: center;
    justify-content: center;
  }
  .side-frame {
    position: absolute;
    left: 16px;
    top: 70px;
    width: 86px;
    height: 700px;
    border: 1px solid var(--lime);
  }
  .side-list {
    position: absolute;
    left: 16px;
    top: 600px;
    width: 88px;
    margin: 0;
    padding: 0;
    list-style: none;
    font-family: "Yanone Kaffeesatz", sans-serif;
    font-size: 16px;
    color: var(--white);
  }
  .side-list li {
    border: 1.5px solid var(--white);
    text-align: center;
    line-height: 30px;
    margin-bottom: 6px;
  }
  .side-brand {
    position: absolute;
    left: 0;
    width: 120px;
    top: 900px;
    margin: 0;
    text-align: center;
    font-family: "Comfortaa", sans-serif;
    font-weight: 700;
    font-size: 15px;
    color: var(--teal);
  }
</style>
</head>
<body>
<main class="canvas">
  <div class="box-panels">

    <section class="panel panel-side side-left" aria-label="Box side panel with text">
      <svg class="panel-art" width="120" height="1000" viewBox="0 0 120 1000">
        <defs>
          <pattern id="sideCopy" width="120" height="22" patternUnits="userSpaceOnUse">
            <text x="6" y="15" font-family="Yanone Kaffeesatz, sans-serif" font-size="14" fill="#ffffff">copy copy copy copy</text>
          </pattern>
        </defs>
        <rect width="120" height="1000" fill="var(--lime)"/>
        <rect x="0" y="60" width="120" height="600" fill="url(#sideCopy)"/>
      </svg>
    </section>

    <section class="panel panel-front" aria-label="NuraLeaf baby probiotic plus vitamin D drops, front panel">
      <svg class="panel-art" width="600" height="1000" viewBox="0 0 600 1000">
        <defs>
          <linearGradient id="babyTone" x1="0" y1="0" x2="0" y2="1">
            <stop offset="0" stop-color="var(--hair)"/>
            <stop offset="0.45" stop-color="var(--skin)"/>
            <stop offset="1" stop-color="var(--shirt)"/>
          </linearGradient>
          <linearGradient id="leafTone" x1="0" y1="0" x2="1" y2="1">
            <stop offset="0" stop-color="var(--leaf)"/>
            <stop offset="1" stop-color="var(--leaf-dark)"/>
          </linearGradient>
        </defs>
        <path class="top-band" d="M0 0 H600 V78 C470 40 300 42 0 86 Z" fill="var(--lime)"/>
        <path class="mid-band" d="M0 560 C150 557 380 566 600 578 V795 C420 797 200 805 0 800 Z" fill="var(--lime)"/>
        <path class="drop-badge" d="M430 390 C455 425 515 455 515 500 A85 85 0 1 1 345 500 C345 455 405 425 430 390 Z" fill="var(--orange)" stroke="var(--white)" stroke-width="8"/>
        <rect class="baby-illustration" x="0" y="385" width="300" height="430" rx="40" fill="url(#babyTone)" role="img" aria-label="Illustration of a smiling baby in a green shirt lying on its tummy"/>
        <rect class="leaf-illustration" x="275" y="790" width="140" height="190" rx="70" fill="url(#leafTone)" role="img" aria-label="Decorative green leaves"/>
      </svg>

      <p class="brand-name"><span class="brand-dot"></span>NuraLeaf</p>
      <h1 class="range-name">baby</h1>
      <h2 class="product-name">Probiotic+Vitamin D</h2>
      <p class="format-label">DROPS</p>
      <p class="benefit">Safe &amp; Effective<br>digestive system &amp;<br>immune system</p>
      <ul class="details">
        <li>copy copy copy</li>
        <li>copy copy copy</li>
        <li>copy copy copy</li>
        <li>copy copy copy</li>
      </ul>
      <p class="dose"><span class="dose-amount">000 IU</span><span class="dose-unit">per drop</span></p>
    </section>

    <section class="panel panel-side side-right" aria-label="Box side panel with details">
      <svg class="panel-art" width="120" height="1000" viewBox="0 0 120 1000">
        <path d="M0 0 H120 V50 C80 44 40 44 0 48 Z" fill="var(--lime)"/>
        <path d="M0 560 H120 V800 H0 Z" fill="var(--lime)"/>
      </svg>
      <div class="side-frame"></div>
      <p class="side-label">copy copy copy</p>
      <ul class="side-list">
        <li>copy copy copy</li>
        <li>copy copy copy</li>
        <li>copy copy copy</li>
        <li>copy copy copy</li>
        <li>copy copy copy</li>
      </ul>
      <p class="side-brand">NuraLeaf</p>
    </section>

  </div>
</main>
</body>
</html>
```